Wild Mo's Wine Label Project

We need a new entry level wine label called "Wild Mo's" for a range of wines we are developing from inland Australia. Our company is made up of three youngish guys who live hard and love taking the mickey. Wild Mo is Wild Moss - the largest and loudest of the three partners (and ideally this label will take the mickey out of him). We've grown the grapes ourselves for this first release which will be a 2012 Pinot Gris. Wine style is dry, young, fresh and contemporary and pitched at the sub AUD $10 retail price point. The package will be flint (clear) claret shape bottle with plain screwcap (colour matched to suit the winning label design).

I've attached a couple of photos of Wild Moss to give you some idea of his presence and persona.

Target Market(s)

Semi educated 25 - 40 year old wine drinkers. Skewed towards females.

Industry/Entity Type

Retail

Requirements
Should not have
• Anything traditional or old fashioned

```html
<!DOCTYPE html>
<html lang="en">
<head>
<meta charset="utf-8">
<title>Wild Mo's Pinot Gris Label</title>
<link href="https://fonts.googleapis.com/css2?family=Abel&display=swap" rel="stylesheet">
<style>
  :root {
    --backdrop: #f6f1ea;
    --label-black: #111111;
    --label-paper: #f2f2f2;
    --panel-light: #e4e4e4;
    --panel-mid: #cfcfcf;
    --ink-dark: #2a2a2a;
  }
  html, body {
    margin: 0;
    padding: 0;
    width: 1200px;
    height: 900px;
    overflow: hidden;
    background: var(--backdrop);
  }
  .canvas {
    position: relative;
    width: 1200px;
    height: 900px;
  }
  .wine-label {
    position: absolute;
    left: 290px;
    top: 150px;
    width: 620px;
    height: 600px;
    display: block;
  }
  .label-wordmark,
  .label-volume,
  .label-variety,
  .label-winery {
    font-family: "Abel", sans-serif;
    fill: var(--ink-dark);
  }
  .label-wordmark { font-size: 168px; }
  .label-volume { font-size: 30px; }
  .label-variety { font-size: 42px; }
  .label-winery { font-size: 42px; }
</style>
</head>
<body>
<main class="canvas">
  <svg class="wine-label" viewBox="0 0 620 600" xmlns="http://www.w3.org/2000/svg" aria-label="Wild Mo's Pinot Gris wine label">
    <defs>
      <linearGradient id="panel-fill" x1="0" y1="0" x2="1" y2="1">
        <stop offset="0" stop-color="var(--panel-light)"/>
        <stop offset="1" stop-color="var(--panel-mid)"/>
      </linearGradient>
    </defs>

    <rect class="label-frame" x="0" y="0" width="620" height="600" fill="var(--label-black)"/>
    <rect class="label-paper" x="0" y="22" width="620" height="520" fill="var(--label-paper)"/>
    <rect class="label-panel" x="300" y="22" width="320" height="430" fill="url(#panel-fill)" role="img" aria-label="Light grey diamond pattern panel"/>

    <text class="label-volume" transform="translate(44 237) rotate(-90)" text-anchor="middle">750 ML 12% VOL</text>

    <text class="label-wordmark" x="86" y="180" textLength="500" lengthAdjust="spacing">WILD</text>
    <text class="label-wordmark" x="86" y="345" textLength="500" lengthAdjust="spacing">MO'S</text>

    <text class="label-variety" x="600" y="425" text-anchor="end">PINOT GRIS</text>

    <rect class="label-rule" x="0" y="452" width="620" height="8" fill="var(--label-black)"/>
    <text class="label-winery" x="14" y="514" textLength="592" lengthAdjust="spacingAndGlyphs">SALTBUSH FLATS WINERY</text>
  </svg>
</main>
</body>
</html>
```